Book cover needed for self help business book

Book cover needed and I will provide back cover blurb and barcode to the winning designer. Book may be too small for spine, but I will give you the page number details to confirm. Book information below:

Title: Nine Winters a Trader
Subtitle: Proven Market Methods That Keep Paying Off Now
Author: Maribel Okonte

Design should be clean, modern, and bold—something that appeals to everyday entrepreneurs and resellers. The cover should reflect grit, real-world hustle, and long-term wisdom without looking overly corporate or flashy. I am open to your creative ideas.

I am open to modern designs, but also designs of rugged old covers that simulate a book that may have aged over the years.

I prefer not to have pictures or silhouettes of people

Requirements
Nice to have
• I am open to modern designs, but also designs of rugged old covers that simulate a book that may have aged over the years.
Should not have
• Pictures or silhouettes of people

```html
<!DOCTYPE html>
<html lang="en">
<head>
<meta charset="utf-8">
<title>Nine Winters a Trader — Book Cover</title>
<link rel="stylesheet" href="https://fonts.googleapis.com/css2?family=Bungee&family=Libre+Baskerville:wght@700&display=swap">
<style>
  :root {
    --backdrop: #414141;
    --paper: #ecdcb5;
    --paper-light: #f6ead0;
    --paper-shade: #dcc69c;
    --title-ink: #6a5744;
    --subtitle-ink: #3d3b3b;
    --author-ink: #85745e;
  }
  html, body {
    margin: 0;
    padding: 0;
    width: 994px;
    height: 1200px;
    overflow: hidden;
    background: var(--backdrop);
  }
  .stage {
    position: relative;
    width: 994px;
    height: 1200px;
  }
  .book-cover {
    position: absolute;
    left: 207px;
    top: 193px;
    width: 579px;
    height: 817px;
    background:
      radial-gradient(ellipse 60% 40% at 20% 30%, var(--paper-light) 0%, transparent 70%),
      radial-gradient(ellipse 50% 35% at 75% 15%, var(--paper-shade) 0%, transparent 70%),
      radial-gradient(ellipse 55% 30% at 60% 70%, var(--paper-light) 0%, transparent 70%),
      radial-gradient(ellipse 40% 30% at 15% 85%, var(--paper-shade) 0%, transparent 70%),
      var(--paper);
    overflow: hidden;
  }
  .cover-type {
    position: absolute;
    inset: 0;
    width: 579px;
    height: 817px;
  }
  .title-word {
    font-family: "Bungee", sans-serif;
    fill: var(--title-ink);
  }
  .author-name {
    font-family: "Bungee", sans-serif;
    fill: var(--author-ink);
  }
  .subtitle {
    position: absolute;
    left: 0;
    right: 0;
    top: 583px;
    margin: 0;
    font-family: "Libre Baskerville", serif;
    font-weight: 700;
    font-size: 18px;
    line-height: 27px;
    color: var(--subtitle-ink);
    text-align: center;
  }
  .subtitle-line {
    display: flex;
    align-items: center;
    justify-content: center;
    gap: 10px;
  }
  .rule-stack {
    display: flex;
    flex-direction: column;
    gap: 3px;
    width: 31px;
  }
  .rule-stack span {
    display: block;
    height: 2px;
    background: var(--subtitle-ink);
  }
</style>
</head>
<body>
<div class="stage">
  <div class="book-cover">
    <svg class="cover-type" viewBox="0 0 579 817" role="group" aria-label="Nine Winters a Trader by Maribel Okonte">
      <text class="title-word" transform="translate(127 422) scale(1 1.65)" x="0" y="0" font-size="190" textLength="318" lengthAdjust="spacingAndGlyphs">NINE</text>
      <text class="title-word" transform="translate(127 483) scale(1 1.4)" x="0" y="0" font-size="52" textLength="323" lengthAdjust="spacingAndGlyphs">WINTERS A</text>
      <text class="title-word" transform="translate(127 544) scale(1 1.2)" x="0" y="0" font-size="62" textLength="323" lengthAdjust="spacingAndGlyphs">TRADER</text>
      <text class="author-name" transform="translate(129 756) scale(1 1.4)" x="0" y="0" font-size="36" textLength="321" lengthAdjust="spacingAndGlyphs">MARIBEL OKONTE</text>
    </svg>
    <p class="subtitle">
      <span class="subtitle-line">Proven Market Methods</span>
      <span class="subtitle-line">
        <span class="rule-stack"><span></span><span></span><span></span></span>
        That Keep Paying Off Now
        <span class="rule-stack"><span></span><span></span><span></span></span>
      </span>
    </p>
  </div>
</div>
</body>
</html>
```